Business Card and Simple Logo Desgin

New Zealand based start up company "Brook Advisory LTD" requires business cards and simple logo design.

Card Content.

Brook Advisory LTD

Joanna Pritchard
CA, BMS (Hons)

j.pritchard@brookadvisory.co.nz
PH +64 21 574 160

Target Market(s)

Corporate Business in IT, Finance and accounting.

Industry/Entity Type

Business

```html
<!DOCTYPE html>
<html lang="en">
<head>
<meta charset="utf-8">
<title>Brook Advisory LTD – Business Card</title>
<link rel="stylesheet" href="https://fonts.googleapis.com/css2?family=Source+Sans+3:wght@400;700&display=swap">
<style>
  :root {
    --brand-red: #f0002a;
    --accent-orange: #ff7a1a;
    --ink: #333333;
    --paper: #ffffff;
    --edge: #7a7a7a;
  }
  html, body {
    margin: 0;
    padding: 0;
    overflow: hidden;
    background: var(--paper);
  }
  .card {
    position: relative;
    width: 1200px;
    height: 695px;
    box-sizing: border-box;
    border: 2px solid var(--edge);
    background: var(--paper);
    font-family: "Source Sans 3", sans-serif;
    overflow: hidden;
  }
  .centered {
    position: absolute;
    transform: translateX(-50%);
    white-space: nowrap;
    text-align: center;
    margin: 0;
    line-height: 1;
  }
  .brand-mark {
    left: 326px;
    top: 118px;
    font-size: 138px;
    font-weight: 700;
    color: var(--brand-red);
  }
  .company-name {
    left: 380px;
    top: 323px;
    font-size: 50px;
    font-weight: 700;
    color: var(--brand-red);
    letter-spacing: 0.5px;
  }
  .person-name {
    left: 380px;
    top: 446px;
    font-size: 34px;
    font-weight: 700;
    color: var(--ink);
  }
  .credentials {
    left: 380px;
    top: 494px;
    font-size: 34px;
    font-weight: 400;
    color: var(--ink);
  }
  .email {
    left: 357px;
    top: 557px;
    font-size: 32px;
    font-weight: 400;
    color: var(--ink);
  }
  .phone {
    left: 357px;
    top: 610px;
    font-size: 32px;
    font-weight: 400;
    color: var(--ink);
  }
  .side-rules {
    position: absolute;
    left: 1040px;
    top: 0;
    width: 72px;
    height: 695px;
  }
</style>
</head>
<body>
  <main class="card">
    <div class="centered brand-mark">Brook</div>
    <h1 class="centered company-name">BROOK ADVISORY LTD</h1>
    <p class="centered person-name">Joanna Pritchard</p>
    <p class="centered credentials">CA, BMS (Hons)</p>
    <p class="centered email">j.pritchard@brookadvisory.co.nz</p>
    <p class="centered phone">PH +64 21 574 160</p>
    <svg class="side-rules" viewBox="0 0 72 695" aria-hidden="true">
      <line x1="11" y1="20" x2="11" y2="695" stroke="var(--accent-orange)" stroke-width="2"/>
      <line x1="36" y1="20" x2="36" y2="695" stroke="var(--accent-orange)" stroke-width="2"/>
      <line x1="61" y1="20" x2="61" y2="695" stroke="var(--accent-orange)" stroke-width="2"/>
    </svg>
  </main>
</body>
</html>
```